Business Card Design Project

Looking for a simple and stylish business card. We are an Advertising Company. The card Must feature the company logo (attached) and also this info.
p: 0481629054
e: sales@rv-promo.com.au
w: www.rv-promo.com.au
We Advertise mainly using TV screens featured in restaurants and cafe. See website for more about the business.
Not really looking for a plain background, but at the same time do not want to much happening in the Background. I am not really to fussy though with the design or the colour scheme, and I am leaving the creativity part up to you creative designers.

```html
<!DOCTYPE html>
<html lang="en">
<head>
<meta charset="utf-8">
<title>RVPROMO – Business Card</title>
<link href="https://fonts.googleapis.com/css2?family=Montserrat:ital,wght@0,300;0,400;0,700;1,700&display=swap" rel="stylesheet">
<style>
  :root {
    --page-bg: #ffffff;
    --card-bg: #ffffff;
    --navy: #1a4a94;
    --pink: #e2215c;
    --globe-tone: #9fc4c8;
    --globe-edge: #8aa3ab;
    --dots-tone: #d3ece0;
  }
  * { margin: 0; padding: 0; box-sizing: border-box; }
  html, body {
    width: 1200px;
    height: 1000px;
    overflow: hidden;
    background: var(--page-bg);
    font-family: "Montserrat", sans-serif;
  }
  .business-card {
    position: absolute;
    left: 222px;
    top: 273px;
    width: 756px;
    height: 432px;
    background: var(--card-bg);
    overflow: hidden;
  }
  .globe-decoration {
    position: absolute;
    left: 0;
    top: 0;
    width: 330px;
    height: 244px;
    background: radial-gradient(ellipse 100% 100% at 0% 40%,
      rgba(138,163,171,0.35) 0%,
      rgba(159,196,200,0.25) 45%,
      rgba(159,196,200,0) 100%);
  }
  .dot-field {
    position: absolute;
    left: 348px;
    top: 158px;
    width: 408px;
    height: 266px;
    background: radial-gradient(ellipse 100% 100% at 100% 30%,
      rgba(211,236,224,0.85) 0%,
      rgba(211,236,224,0.4) 55%,
      rgba(211,236,224,0) 100%);
  }
  .brand-name {
    position: absolute;
    left: 0;
    width: 756px;
    top: 70px;
    text-align: center;
    font-weight: 400;
    font-size: 78px;
    line-height: 1;
    letter-spacing: 2px;
    color: var(--navy);
  }
  .contact-list {
    position: absolute;
    left: 37px;
    top: 309px;
    list-style: none;
    font-size: 21px;
    line-height: 33px;
    color: var(--navy);
  }
  .contact-label { font-weight: 300; }
  .contact-value { font-weight: 700; }
  .person {
    position: absolute;
    right: 38px;
    top: 339px;
    text-align: right;
    color: var(--pink);
    font-size: 23px;
    line-height: 33px;
  }
  .person-role { font-weight: 700; font-style: italic; }
  .person-name { font-weight: 400; }
</style>
</head>
<body>
  <div class="business-card">
    <div class="globe-decoration" role="img" aria-label="Faint wireframe globe decoration fading into the card"></div>
    <div class="dot-field" role="img" aria-label="Soft field of small mint diamond dots"></div>

    <div class="brand-name">RVPROMO</div>

    <ul class="contact-list">
      <li><span class="contact-label">p:</span> <span class="contact-value">0481629054</span></li>
      <li><span class="contact-label">e:</span> <span class="contact-value">sales@rv-promo.com.au</span></li>
      <li><span class="contact-label">w:</span> <span class="contact-value">www.rv-promo.com.au</span></li>
    </ul>

    <div class="person">
      <div class="person-role">Managing Director</div>
      <div class="person-name">Mark Tessaro</div>
    </div>
  </div>
</body>
</html>
```